All natural lip balm label

Need a label design for a new all natural bath and body company (mybrenvale.com). We provide natural alternatives to harsh bath and body products. We have a lip balm that needs a new design!

I have attached my facebook cover photo because it might help with the design. But you do not have to use that.

Target Market(s)

people 30-55

Industry/Entity Type

It Company

Requirements
Must have
• Name of company is Brena Vale Bath & Body

must have "All Natural Lip Balm" near the logo

Must be in adobe illustrator EPS form (300 dpi) with 4 files (one for each flavor of lip balm: Herbal Mint, Cherry, Vanilla, Peppermint).
See details to art specs on my printer's site: http://www.quorvatags.com/artspecs.htm (note that the text needs to be "outlined")

must be in the following size: 2.125000 x 2.125000 (2-1/8 x 2-1/8)

must have ingredients as shown below...
Ingredients: Organic Glycine Soja (soybean) Oil, Helianthus Annuus (sunflower) Seed Oil, Palm (Elaeis Guineensis) Oil, organic Olea Europaea (Olive) Fruit Oil, Avocado (Persea Gratissima) Oil, Beeswax (Cera Alba), Cocoa (Theobroma Cacao) Seed Butter, Shea Butter (Butyrospermum Parkii), Tocopherol Pure Vitamin E, Natural Flavor

Must have size of product on the label: "0.15 oz/4.25 g"

Must have following verbiage:
distributed by BrenaVale Bath & Body
Dunmere, WI 58407
www.mybrenvale.com

must use the attached logo in some fashion (see "small logo" in attached files)
Nice to have
• use your imagination!

```html
<!DOCTYPE html>
<html lang="en">
<head>
<meta charset="utf-8">
<title>Brena Vale – All Natural Lip Balm Labels</title>
<link rel="stylesheet" href="https://fonts.googleapis.com/css2?family=Ubuntu:ital,wght@0,400;0,700;1,700&display=swap">
<style>
  :root {
    --page: #ffffff;
    --herbal: #3f8a2a;
    --herbal-soft: #cfe3c2;
    --cherry: #c0143c;
    --cherry-soft: #f3c9d3;
    --peppermint: #17907c;
    --peppermint-soft: #c3e6df;
    --vanilla: #b3a455;
    --vanilla-soft: #ece6c4;
    --label-base: #fbfbf8;
  }
  * { box-sizing: border-box; margin: 0; padding: 0; }
  html, body {
    width: 1200px; height: 900px; overflow: hidden;
    background: var(--page);
    font-family: "Ubuntu", sans-serif;
  }
  .label-row { position: relative; width: 1200px; height: 900px; }
  .label {
    position: absolute; top: 335px;
    width: 130px; height: 330px;
    overflow: hidden;
    background: var(--label-base);
    color: var(--ink);
  }
  .label--herbal { left: 218px; --ink: var(--herbal); --soft: var(--herbal-soft); }
  .label--cherry { left: 425px; --ink: var(--cherry); --soft: var(--cherry-soft); }
  .label--peppermint { left: 632px; --ink: var(--peppermint); --soft: var(--peppermint-soft); }
  .label--vanilla { left: 838px; --ink: var(--vanilla); --soft: var(--vanilla-soft); }

  .label__wash {
    position: absolute; inset: 0;
    background:
      linear-gradient(160deg, transparent 30%, var(--soft) 48%, transparent 62%),
      linear-gradient(200deg, var(--label-base) 20%, var(--soft) 55%, var(--label-base) 85%);
    opacity: .9;
  }
  .label__turned {
    position: absolute;
    left: -62.5px; top: 62.5px;
    width: 255px; height: 130px;
    transform: rotate(90deg);
    padding: 6px 6px 4px 14px;
    display: flex; flex-direction: column; justify-content: space-between;
  }
  .label__ingredients {
    font-size: 6.4px; line-height: 8px; opacity: .85;
    white-space: nowrap; overflow: hidden;
  }
  .brand { display: flex; align-items: center; gap: 6px; margin-left: 26px; }
  .brand__dot {
    width: 16px; height: 16px; border-radius: 50%;
    border: 2px solid var(--ink);
  }
  .brand__name { font-size: 22px; font-weight: 700; letter-spacing: .2px; }
  .brand__tagline { font-size: 10px; font-weight: 700; margin-left: 48px; margin-top: 2px; }
  .label__maker { font-size: 7.6px; line-height: 9px; font-weight: 700; }
  .label__maker span { display: block; font-weight: 400; font-size: 6.6px; line-height: 8px; }

  .label__flavor {
    position: absolute; left: 0; right: 0; bottom: 12px;
    display: flex; flex-direction: column; align-items: center; gap: 8px;
  }
  .flavor__mark { width: 24px; height: 24px; }
  .flavor__name { font-size: 8px; font-weight: 700; font-style: italic; }
</style>
</head>
<body>
<main class="label-row">

  <section class="label label--herbal">
    <div class="label__wash"></div>
    <div class="label__turned">
      <p class="label__ingredients">Seed Butter, Shea Butter (Butyrospermum Parkii), Tocopherol<br>Pure Vitamin E, Natural Flavor</p>
      <div>
        <div class="brand"><span class="brand__dot"></span><span class="brand__name">Brena Vale</span></div>
        <p class="brand__tagline">All natural lip balm</p>
      </div>
      <p class="label__maker">Brena Vale Bath &amp; Body<span>distributed by BrenaVale Bath &amp; Body<br>Dunmere, WI 58407 · www.mybrenvale.com</span></p>
    </div>
    <div class="label__flavor">
      <svg class="flavor__mark" viewBox="0 0 24 24" role="img" aria-label="Herbal mint leaf icon"><circle cx="12" cy="12" r="11" fill="var(--herbal)"/></svg>
      <span class="flavor__name">Herbal Mint</span>
    </div>
  </section>

  <section class="label label--cherry">
    <div class="label__wash"></div>
    <div class="label__turned">
      <p class="label__ingredients">Seed Butter, Shea Butter (Butyrospermum Parkii), Tocopherol<br>Pure Vitamin E, Natural Flavor</p>
      <div>
        <div class="brand"><span class="brand__dot"></span><span class="brand__name">Brena Vale</span></div>
        <p class="brand__tagline">All natural lip balm</p>
      </div>
      <p class="label__maker">Brena Vale Bath &amp; Body<span>distributed by BrenaVale Bath &amp; Body<br>Dunmere, WI 58407 · www.mybrenvale.com</span></p>
    </div>
    <div class="label__flavor">
      <svg class="flavor__mark" viewBox="0 0 24 24" role="img" aria-label="Cherry icon"><circle cx="12" cy="13" r="10" fill="var(--cherry)"/></svg>
      <span class="flavor__name">Cherry</span>
    </div>
  </section>

  <section class="label label--peppermint">
    <div class="label__wash"></div>
    <div class="label__turned">
      <p class="label__ingredients">Seed Butter, Shea Butter (Butyrospermum Parkii), Tocopherol<br>Pure Vitamin E, Natural Flavor</p>
      <div>
        <div class="brand"><span class="brand__dot"></span><span class="brand__name">Brena Vale</span></div>
        <p class="brand__tagline">All natural lip balm</p>
      </div>
      <p class="label__maker">Brena Vale Bath &amp; Body<span>distributed by BrenaVale Bath &amp; Body<br>Dunmere, WI 58407 · www.mybrenvale.com</span></p>
    </div>
    <div class="label__flavor">
      <svg class="flavor__mark" viewBox="0 0 24 24" role="img" aria-label="Peppermint leaves icon"><circle cx="12" cy="12" r="11" fill="var(--peppermint)"/></svg>
      <span class="flavor__name">Peppermint</span>
    </div>
  </section>

  <section class="label label--vanilla">
    <div class="label__wash"></div>
    <div class="label__turned">
      <p class="label__ingredients">Seed Butter, Shea Butter (Butyrospermum Parkii), Tocopherol<br>Pure Vitamin E, Natural Flavor</p>
      <div>
        <div class="brand"><span class="brand__dot"></span><span class="brand__name">Brena Vale</span></div>
        <p class="brand__tagline">All natural lip balm</p>
      </div>
      <p class="label__maker">Brena Vale Bath &amp; Body<span>distributed by BrenaVale Bath &amp; Body<br>Dunmere, WI 58407 · www.mybrenvale.com</span></p>
    </div>
    <div class="label__flavor">
      <svg class="flavor__mark" viewBox="0 0 24 24" role="img" aria-label="Vanilla pods icon"><rect x="9" y="1" width="6" height="22" rx="3" fill="var(--vanilla)"/></svg>
      <span class="flavor__name">Vanilla</span>
    </div>
  </section>

</main>
</body>
</html>
```